Lumo4Kart - a fintech company - business card

We need a business card design for our Payments Technology company in Sydney, Australia. We provide business with payment solutions expanding across EFTPOS machines, online payment gateways and mobile payment solutions. We would like to see designs that are clean, classy and professional.
Target Market(s)
Business professionals, executives, c-suite
Industry/Entity Type
Fintech
Contact Information for Business Card
Will be on 400gsm. Logo will most likely be spot gloss unless designer recommends otherwise.
Font styles to use
Sans Serif
Requirements
Must have
- We need our website (lumo4kart.com.au), email (contact@lumo4kart.com.au), mobile (0432 587 904) and direct phone number (02 6815 3927) to feature on the card along with our logo (attached) and the words "EFTPOS | ONLINE | MOBILE"
- Font = Roboto

```html
<!DOCTYPE html>
<html lang="en">
<head>
<meta charset="utf-8">
<title>Lumo4Kart – Business Card</title>
<link rel="stylesheet" href="https://fonts.googleapis.com/css2?family=Roboto:wght@300;400;500;700&display=swap">
<style>
  :root {
    --brand-blue: #1a5f8e;
    --ink-grey: #5c5e62;
    --paper: #ffffff;
    --paper-shade: #f1f1f2;
    --fold-shade: #d9d9db;
    --backdrop: #2c2c2e;
  }
  * { box-sizing: border-box; margin: 0; padding: 0; }
  html, body {
    width: 1200px; height: 900px; overflow: hidden;
    background: var(--backdrop);
    font-family: "Roboto", Arial, sans-serif;
  }
  .stage {
    position: relative; width: 1200px; height: 900px;
    display: flex; flex-direction: column; align-items: center; justify-content: center; gap: 40px;
  }
  .card {
    position: relative; width: 700px; height: 400px;
    background: var(--paper); border-radius: 16px; overflow: hidden;
  }
  .card__halo { position: absolute; border-radius: 50%; background: var(--paper-shade); }

  .brand-name { font-weight: 500; color: var(--ink-grey); letter-spacing: 0; }

  /* Front */
  .card--front .card__halo { width: 560px; height: 560px; left: 70px; top: -80px; }
  .front-brand {
    position: absolute; left: 0; right: 0; top: 150px;
    display: flex; justify-content: center;
  }
  .front-brand .brand-name { font-size: 46px; line-height: 1; }
  .tagline {
    position: absolute; left: 0; right: 0; bottom: 42px; text-align: center;
    font-weight: 400; font-size: 13px; letter-spacing: 3px; color: var(--brand-blue);
  }

  /* Back */
  .card--back .card__halo { width: 520px; height: 520px; left: 330px; top: -150px; }
  .block { position: absolute; left: 0; background: var(--brand-blue); }
  .block--top { top: 0; width: 255px; height: 135px; }
  .block--bottom { top: 265px; width: 360px; height: 135px; }
  .band {
    position: absolute; left: 0; top: 135px; width: 300px; height: 130px;
    background: var(--paper-shade);
    display: flex; align-items: center; justify-content: center;
  }
  .band__fold {
    position: absolute; right: -30px; top: 0; width: 0; height: 0;
    border-top: 130px solid var(--fold-shade); border-right: 30px solid transparent;
  }
  .band .brand-name { font-size: 30px; }

  .contact-rail {
    position: absolute; left: 402px; top: 90px; width: 3px; height: 310px; background: var(--brand-blue);
  }
  .contact-list { position: absolute; left: 385px; top: 80px; list-style: none; }
  .contact-item {
    display: flex; align-items: center; gap: 14px; height: 38px; margin-bottom: 26px;
    font-size: 18px; font-weight: 500; color: var(--brand-blue); white-space: nowrap;
  }
  .contact-icon {
    width: 38px; height: 38px; border-radius: 50%; background: var(--brand-blue);
    display: flex; align-items: center; justify-content: center; flex-shrink: 0;
    box-shadow: 0 0 0 3px var(--paper);
  }
  .contact-icon svg { width: 20px; height: 20px; }
</style>
</head>
<body>
<main class="stage">
  <section class="card card--front" aria-label="Business card front">
    <div class="card__halo"></div>
    <div class="front-brand">
      <div class="brand-name">Lumo4Kart</div>
    </div>
    <div class="tagline">EFTPOS | ONLINE | MOBILE</div>
  </section>

  <section class="card card--back" aria-label="Business card back">
    <div class="card__halo"></div>
    <div class="block block--top"></div>
    <div class="band">
      <div class="brand-name">Lumo4Kart</div>
      <div class="band__fold"></div>
    </div>
    <div class="block block--bottom"></div>

    <div class="contact-rail"></div>
    <ul class="contact-list">
      <li class="contact-item">
        <span class="contact-icon">
          <svg viewBox="0 0 20 20" fill="none" stroke="#fff" stroke-width="1.6"><rect x="5.5" y="2" width="9" height="16" rx="1.5"/><line x1="9" y1="15.5" x2="11" y2="15.5"/></svg>
        </span>
        <span>0432 587 904</span>
      </li>
      <li class="contact-item">
        <span class="contact-icon">
          <svg viewBox="0 0 20 20" fill="#fff"><path d="M5 2.5l2.8 3.2-1.6 2c.9 2 2.3 3.4 4.1 4.2l2-1.6 3.2 2.8-1.4 2.6c-5.7-.3-10.6-5.2-10.9-10.9z"/></svg>
        </span>
        <span>02 6815 3927</span>
      </li>
      <li class="contact-item">
        <span class="contact-icon">
          <svg viewBox="0 0 20 20" fill="none" stroke="#fff" stroke-width="1.5"><rect x="2.5" y="5" width="15" height="10.5"/><polyline points="2.5,5 10,11 17.5,5"/></svg>
        </span>
        <span>contact@lumo4kart.com.au</span>
      </li>
      <li class="contact-item">
        <span class="contact-icon">
          <svg viewBox="0 0 20 20" fill="none" stroke="#fff" stroke-width="1.3"><circle cx="10" cy="10" r="7.5"/><ellipse cx="10" cy="10" rx="3.3" ry="7.5"/><line x1="2.5" y1="10" x2="17.5" y2="10"/><line x1="3.8" y1="6" x2="16.2" y2="6"/><line x1="3.8" y1="14" x2="16.2" y2="14"/></svg>
        </span>
        <span>lumo4kart.com.au</span>
      </li>
    </ul>
  </section>
</main>
</body>
</html>
```